Velmora Partners - website for real estate investment company

Create a bold, modern website that reflects Velmora’s success, professionalism, and credibility.
The design must stand out while maintaining a polished, corporate tone. (bold, but understated)
The client just created a new logo, and the website design must be in sync with the logo design. Information about the logo colors, fonts, and message are in the attached design brief.
Updates

Target Market(s)

b2b: banks, brokers, institutional partners, vendors, and property sellers.

Industry/Entity Type

real estate investment company

Number of Pages Required

1 page

Font styles to use
Sans Serif

Colors

Designer to choose colors to be used in the design.

Requirements
Must have
• 1. homepage design (psd) 2. a top banner image (psd) for a default inner page
Nice to have
• please see attached design brief
Should not have

```html
<!DOCTYPE html>
<html lang="en">
<head>
<meta charset="utf-8">
<title>Velmora Partners — Real Estate Investment</title>
<link href="https://fonts.googleapis.com/css2?family=Barlow:wght@400;500;600;700;800&family=Barlow+Condensed:wght@600;700&family=Poppins:wght@400;500;600&display=swap" rel="stylesheet">
<style>
:root{
  --red:#e0202a;
  --red-dark:#b8141d;
  --ink:#222222;
  --text:#555555;
  --muted:#777777;
  --dark:#1d1d1f;
  --charcoal:#4a4a4c;
  --blush:#fdeeee;
  --line:#e6e6e6;
  --white:#ffffff;
  --navy:#1b3a6b;
}
*{box-sizing:border-box;margin:0;padding:0}
html,body{width:1200px;height:4777px;overflow:hidden}
body{font-family:"Poppins",sans-serif;color:var(--text);background:var(--white);position:relative}
.abs{position:absolute}
h1,h2,h3,h4{font-family:"Barlow",sans-serif;color:var(--ink)}
.red{color:var(--red)}

/* header */
.site-header{position:absolute;top:0;left:0;width:1200px;height:80px;background:var(--white);border-bottom:1px solid var(--line)}
.brand{position:absolute;left:143px;top:20px;font-family:"Barlow",sans-serif;font-weight:800;font-size:38px;letter-spacing:1px;color:var(--charcoal);display:flex;align-items:center;gap:8px}
.brand .mark{width:12px;height:12px;background:var(--red);border-radius:50%}
.nav{position:absolute;left:410px;top:31px;display:flex;gap:17px;font-family:"Barlow",sans-serif;font-weight:600;font-size:12px;color:var(--ink);text-transform:uppercase}
.nav-cta{position:absolute;left:943px;top:18px;width:116px;height:44px;border-radius:22px;background:var(--red);color:#fff;font-family:"Barlow",sans-serif;font-weight:600;font-size:12px;display:flex;align-items:center;justify-content:center}

/* hero */
.hero{position:absolute;top:80px;left:0;width:1200px;height:565px;background:linear-gradient(100deg,#151515 0%,#2a2a2a 35%,#6b6560 70%,#a49a8f 100%)}
.hero-title{position:absolute;left:143px;top:142px;color:#fff;font-family:"Barlow",sans-serif;line-height:1}
.hero-title .l1{font-weight:400;font-size:52px;letter-spacing:1px}
.hero-title .l2{font-weight:800;font-size:52px;margin-top:14px}
.hero-copy{position:absolute;left:145px;top:275px;width:440px;color:#e8e8e8;font-size:12.5px;line-height:21px}
.btn{display:inline-flex;align-items:center;justify-content:center;border-radius:24px;font-family:"Barlow",sans-serif;font-weight:600;font-size:12px;text-transform:uppercase}
.hero .b1{position:absolute;left:143px;top:384px;width:198px;height:46px;background:var(--red);color:#fff}
.hero .b2{position:absolute;left:353px;top:384px;width:152px;height:46px;background:#fff;color:var(--ink)}

/* section titles */
.tick{width:10px;height:24px;background:var(--charcoal);display:inline-block}
.sec-title{position:absolute;left:0;width:1200px;text-align:center;font-family:"Barlow",sans-serif;font-size:28px;font-weight:500;color:var(--ink);display:flex;justify-content:center;align-items:center;gap:10px}
.sec-title b{color:var(--red);font-weight:600}
.sec-sub{position:absolute;left:300px;width:600px;text-align:center;font-size:15px;line-height:22px;color:var(--ink)}

/* about */
.about-tri{left:124px;top:723px;width:45px;height:45px;background:linear-gradient(135deg,#f4a9ac 50%,transparent 50%)}
.about-photo1{left:143px;top:745px;width:393px;height:420px;background:linear-gradient(180deg,#9cc3e6 0%,#5a7fa6 45%,#1f3448 100%)}
.about-photo2{left:377px;top:996px;width:193px;height:191px;background:linear-gradient(150deg,#f2f2f4 0%,#b9bfc9 55%,#5b6472 100%);border:6px solid #fff;box-shadow:0 6px 20px rgba(0,0,0,.15)}
.about-text{left:608px;top:762px;width:450px}
.about-text h2{font-size:28px;font-weight:500;display:flex;gap:10px;align-items:center}
.about-text h2 b{color:var(--red);font-weight:600}
.about-text .kicker{font-size:17px;color:var(--ink);margin:14px 0 16px;font-family:"Barlow",sans-serif;font-weight:500}
.about-text p{font-size:12.5px;line-height:20px;margin-bottom:10px}
.bullets{list-style:none;margin-top:14px}
.bullets li{font-size:13px;color:var(--ink);margin-bottom:17px;display:flex;gap:14px;align-items:center}
.bullets li::before{content:"";width:0;height:0;border-left:6px solid transparent;border-right:6px solid transparent;border-bottom:12px solid var(--red)}
.about-btn{left:608px;top:1114px;width:208px;height:42px;background:var(--red);color:#fff;font-size:14px;display:flex;align-items:center;justify-content:center;font-weight:500}
.about-btn-tri{left:812px;top:1114px;width:40px;height:42px;background:linear-gradient(to top left,#4a4a4c 50%,transparent 50%)}

/* strategy */
.card{position:absolute;background:#fff;border:1px solid #e4e4e4;border-radius:4px;box-shadow:0 8px 22px rgba(0,0,0,.08);overflow:hidden}
.strat{top:1547px;width:285px;height:247px;padding:30px 22px}
.strat::after{content:"";position:absolute;right:-30px;bottom:-30px;width:130px;height:130px;border-radius:50%;background:rgba(0,0,0,.04)}
.strat h3{font-size:19px;font-weight:600;margin:20px 0 14px}
.strat p{font-size:12px;line-height:19.5px;position:relative;z-index:1}
.strat.dark{background:#5b5b5d;border-color:#5b5b5d}
.strat.dark h3,.strat.dark p{color:#fff}
.strat.dark::after{background:rgba(255,255,255,.06)}

/* stats */
.stats{left:0;top:1879px;width:1200px;height:189px;background:linear-gradient(90deg,#d41e27,#e4323a 50%,#c81821)}
.stat{position:absolute;top:55px;width:250px;text-align:center;color:#fff}
.stat .n{font-family:"Barlow Condensed",sans-serif;font-weight:700;font-size:42px;line-height:1}
.stat .t{font-size:15px;margin-top:16px}
.stat-sep{position:absolute;top:55px;width:1px;height:95px;background:rgba(255,255,255,.35)}
.stats-notch{left:588px;top:2068px;width:0;height:0;border-left:14px solid transparent;border-right:14px solid transparent;border-top:14px solid #d12029}

/* apart */
.apart-bg{left:0;top:2068px;width:1200px;height:498px;background:var(--blush)}
.apart{top:2241px;width:283px;height:226px;padding:26px 24px;text-align:center;overflow:visible}
.apart h3{font-size:19px;font-weight:500;margin:16px 0 12px}
.apart h3 b{color:var(--red);font-weight:600}
.apart p{font-size:11.5px;line-height:19px}
.circle-btn{position:absolute;left:50%;bottom:-20px;margin-left:-20px;width:40px;height:40px;border-radius:50%;background:var(--red);display:flex;align-items:center;justify-content:center}
.circle-btn.grey{background:var(--charcoal)}

/* portfolio */
.port{top:2760px;width:282px;height:347px;border-radius:2px}
.port .ph{height:176px}
.port h3{font-size:18px;font-weight:500;padding:16px 16px 8px;white-space:nowrap}
.port h3 b{color:var(--red);font-weight:600}
.port p{font-size:10.5px;line-height:19px;padding:0 16px}
.port .meta{position:absolute;left:16px;right:16px;bottom:20px;display:flex;justify-content:space-between;font-size:10.5px;color:var(--muted);white-space:nowrap}
.port .meta span:last-child{color:var(--ink);font-weight:600;text-decoration:underline}

/* testimonials */
.testi-bg{left:0;top:3250px;width:1200px;height:488px;background:linear-gradient(90deg,#3d3d3f,#5a5a5c 50%,#3d3d3f)}
.testi-title{left:0;top:3322px;width:1200px;text-align:center;color:#fff;font-family:"Barlow",sans-serif;font-weight:600;font-size:27px}
.tcard{position:absolute;top:3376px;width:284px;height:258px;background:#fff;border-radius:3px;padding:20px 22px;overflow:hidden}
.avatar{width:58px;height:58px;border-radius:50%;background:linear-gradient(160deg,#d9dde2,#8f97a2)}
.stars{position:absolute;left:106px;top:43px;color:var(--red);font-size:17px;letter-spacing:3px}
.quote{position:absolute;right:20px;top:20px;width:30px;height:30px;border-radius:50%;border:2px solid var(--charcoal);color:var(--charcoal);font-family:"Barlow",sans-serif;font-weight:800;font-size:20px;display:flex;align-items:center;justify-content:center;line-height:1}
.quote.r{border-color:var(--red);color:var(--red)}
.tcard h4{font-family:"Poppins",sans-serif;font-weight:500;font-size:13px;margin:16px 0 8px}
.tcard p{font-size:11px;line-height:20px}
.pager{left:572px;top:3652px;display:flex;gap:6px}
.pager i{width:7px;height:7px;border-radius:50%;background:#9a9a9a;display:block}
.pager i.on{background:#fff}

/* contact */
.form-card{left:143px;top:3825px;width:475px;height:458px;border:1px solid #e0e0e0;border-radius:4px;background:#fff;box-shadow:0 6px 20px rgba(0,0,0,.06);padding:30px 30px}
.form-card h2{font-size:25px;font-weight:600;color:var(--charcoal)}
.form-card label{display:block;font-size:13px;color:var(--navy);margin:28px 0 12px 7px}
.form-card label:first-of-type{margin-top:22px}
.field{height:40px;background:#f1f1f1;border-radius:2px}
.field.tall{height:80px}
.submit{margin-top:22px;height:46px;background:var(--charcoal);color:#fff;font-size:14px;font-weight:600;display:flex;align-items:center;justify-content:center;border-radius:2px}
.contact-text{left:651px;top:3876px;width:410px}
.contact-text h2{font-size:25px;font-weight:600}
.contact-text .lead{font-size:13px;color:var(--navy);line-height:22px;margin:12px 0 34px}
.contact-text h4{font-family:"Poppins",sans-serif;font-size:15px;font-weight:500;margin-bottom:14px}
.why{display:flex;gap:14px;margin-bottom:22px}
.why strong{display:block;font-size:12.5px;color:var(--navy);font-weight:500;margin-bottom:4px}
.why span{font-size:12px;line-height:20px;color:#7a7f88}

/* footer */
.footer{left:0;top:4439px;width:1200px;height:338px;background:#1b1b1c;color:#d9d9d9}
.footer .brand{left:145px;top:42px;color:#fff;font-size:40px;position:absolute}
.footer .about{position:absolute;left:145px;top:110px;width:200px;font-size:12.5px;line-height:21px;color:#e4e4e4}
.follow{position:absolute;left:145px;top:185px;font-size:12.5px;display:flex;align-items:center;gap:10px}
.follow i{width:22px;height:22px;border-radius:50%;background:#333;display:block}
.follow i.r{background:var(--red)}
.fcol{position:absolute;top:44px}
.fcol h4{color:#fff;font-family:"Poppins",sans-serif;font-weight:600;font-size:14px;margin-bottom:28px}
.fcol li{list-style:none;font-size:12.5px;margin-bottom:14px}
.fcol li::before{content:"› ";color:var(--red)}
.contact-row{display:flex;align-items:center;gap:20px;font-size:12.5px;margin-bottom:22px;white-space:nowrap}
.contact-row b{color:#fff;font-weight:600}
.contact-row .ic{width:34px;height:34px;border-radius:50%;background:#2d2d2e;display:flex;align-items:center;justify-content:center}
.contact-row .ic.r{background:var(--red)}
.copy{position:absolute;left:0;width:1200px;top:304px;text-align:center;font-size:11px;color:#bdbdbd}
</style>
</head>
<body>

<header class="site-header">
  <div class="brand"><span class="mark"></span>VELMORA</div>
  <nav class="nav"><span>Home</span><span>Our Story</span><span>Investment Strategy</span><span>What Sets Us Apart</span><span>Portfolio</span></nav>
  <div class="nav-cta">CONTACT US</div>
</header>

<section class="hero" role="img" aria-label="Investor signing documents beside a small model house on a desk">
  <div class="hero-title"><div class="l1">EXPERIENCE</div><div class="l2">STRATEGY-VISION</div></div>
  <p class="hero-copy">Velmora Partners Is A Vertically Integrated Real Estate Investment Firm With A Proven Four-Decade Track Record. We Acquire, Reposition, And Operate High-Performing Assets Across Multiple Sectors — Always With A Focus On Exceptional, Risk-Adjusted Returns.</p>
  <span class="btn b1">Explore Our Portfolio</span>
  <span class="btn b2">Partner With Us</span>
</section>

<!-- About -->
<div class="abs about-tri"></div>
<div class="abs about-photo1" role="img" aria-label="Glass office towers against a blue sky"></div>
<div class="abs about-photo2" role="img" aria-label="Business team reviewing charts on a laptop"></div>
<div class="abs about-text">
  <h2><span class="tick"></span><b>ABOUT</b> VELMORA</h2>
  <div class="kicker">40 Years of Real Estate Excellence</div>
  <p>Since 1989, Velmora Partners has established itself as a leader in the real estate investment sector. Our journey began with a commitment to excellence and a vision to transform properties into valuable assets.</p>
  <p>Over four decades, we've refined our approach, building a reputation for integrity, strategic insight, and operational excellence. Our team combines deep industry knowledge with innovative thinking to identify opportunities others overlook.</p>
  <ul class="bullets"><li>Building Value. Creating Opportunity.</li><li>Investing with Vision, Delivering with Confidence.</li></ul>
</div>
<div class="abs about-btn">Our Investment Strategy</div>
<div class="abs about-btn-tri"></div>

<svg class="abs" style="left:0;top:1247px" width="1200" height="98" viewBox="0 0 1200 98">
  <polygon points="0,0 1200,98 0,98" fill="#ececec"/>
  <polygon points="1200,0 1200,98 690,98" fill="#fde3e4"/>
</svg>

<!-- Investment strategy -->
<h2 class="sec-title" style="top:1426px"><span class="tick"></span><b>INVESTMENT</b> STRATEGY</h2>
<p class="sec-sub" style="top:1473px">Velmora Partners is a vertically integrated real estate investment firm with a proven four-decade track record.</p>

<div class="card strat" style="left:143px">
  <svg width="40" height="36" viewBox="0 0 40 36" fill="none" stroke="#e0202a" stroke-width="2"><path d="M8 4h24l6 9-18 20L2 13z"/><path d="M2 13h36M14 4l-4 9 10 20 10-20-4-9"/></svg>
  <h3>Value <span class="red">Identification</span></h3>
  <p>Our in-house acquisition, development, and management teams work seamlessly to execute comprehensive repositioning strategies efficiently and effectively.</p>
</div>
<div class="card strat dark" style="left:457px">
  <svg width="40" height="40" viewBox="0 0 40 40" fill="none" stroke="#fff" stroke-width="3"><circle cx="20" cy="20" r="7"/><path d="M20 3v6M20 31v6M3 20h6M31 20h6M8 8l4 4M28 28l4 4M8 32l4-4M28 12l4-4"/></svg>
  <h3>Vertical Integration</h3>
  <p>Our in-house acquisition, development, and management teams work seamlessly to execute comprehensive repositioning strategies efficiently and effectively.</p>
</div>
<div class="card strat" style="left:773px">
  <svg width="40" height="40" viewBox="0 0 40 40" fill="none" stroke="#e0202a" stroke-width="2"><circle cx="20" cy="20" r="17"/><path d="M13 27l14-14"/><circle cx="14" cy="14" r="3"/><circle cx="26" cy="26" r="3"/></svg>
  <h3>Get an <span class="red">Offer</span></h3>
  <p>We prioritize investments that balance strong potential returns with prudent risk management, ensuring stability and consistency for our partners.</p>
</div>

<!-- Stats -->
<section class="abs stats" role="img" aria-label="Red band with a faint handshake image">
  <div class="stat" style="left:68px"><div class="n">1989</div><div class="t">Founded</div></div>
  <div class="stat-sep" style="left:278px"></div>
  <div class="stat" style="left:313px"><div class="n">23,000+</div><div class="t">Multifamily &amp; Healthcare Units</div></div>
  <div class="stat-sep" style="left:598px"></div>
  <div class="stat" style="left:608px"><div class="n">$300M+</div><div class="t">Invested in Renovations</div></div>
  <div class="stat-sep" style="left:868px"></div>
  <div class="stat" style="left:854px"><div class="n">40+</div><div class="t">Year of experience</div></div>
</section>
<div class="abs stats-notch"></div>

<!-- What sets us apart -->
<div class="abs apart-bg"></div>
<h2 class="sec-title" style="top:2146px"><span class="tick"></span><b>WHAT SETS</b> US APART</h2>
<p class="sec-sub" style="top:2189px">Velmora Partners is a vertically integrated real estate investment.</p>

<div class="card apart" style="left:143px">
  <svg width="44" height="44" viewBox="0 0 44 44" fill="none" stroke="#e0202a" stroke-width="2"><circle cx="22" cy="24" r="14"/><path d="M22 16l3 6 6 1-4 4 1 6-6-3-6 3 1-6-4-4 6-1z"/></svg>
  <h3>Four Decades of <b>Experience</b></h3>
  <p>Our extensive market experience through multiple economic cycles provides invaluable perspective and strategic insight.</p>
  <span class="circle-btn"><svg width="14" height="14" viewBox="0 0 14 14" stroke="#fff" stroke-width="2" fill="none"><path d="M3 11L11 3M5 3h6v6"/></svg></span>
</div>
<div class="card apart" style="left:459px">
  <svg width="50" height="44" viewBox="0 0 50 44" fill="none" stroke="#e0202a" stroke-width="2"><circle cx="25" cy="14" r="5"/><circle cx="11" cy="20" r="4"/><circle cx="39" cy="20" r="4"/><path d="M15 36c0-7 4-12 10-12s10 5 10 12M3 36c0-5 3-9 8-9M47 36c0-5-3-9-8-9M2 40h46"/></svg>
  <h3>Partnership <b>Approach</b></h3>
  <p>We build long-term relationships based on transparency, trust, and mutual success with all stakeholders.</p>
  <span class="circle-btn grey"><svg width="14" height="14" viewBox="0 0 14 14" stroke="#fff" stroke-width="2" fill="none"><path d="M3 11L11 3M5 3h6v6"/></svg></span>
</div>
<div class="card apart" style="left:775px">
  <svg width="40" height="44" viewBox="0 0 40 44" fill="none" stroke="#e0202a" stroke-width="2"><path d="M20 4a12 12 0 0 0-7 22v6h14v-6A12 12 0 0 0 20 4z"/><path d="M14 36h12M16 40h8"/></svg>
  <h3>Innovative <b>Solutions</b></h3>
  <p>We combine traditional real estate expertise with cutting-edge technology and data analytics to drive performance.</p>
  <span class="circle-btn"><svg width="14" height="14" viewBox="0 0 14 14" stroke="#fff" stroke-width="2" fill="none"><path d="M3 11L11 3M5 3h6v6"/></svg></span>
</div>

<!-- Portfolio -->
<h2 class="sec-title" style="top:2641px"><span class="tick"></span><b>OUR</b> PORTFOLIO</h2>
<p class="sec-sub" style="top:2688px">A diverse portfolio of high-performing assets across multifamily and healthcare sectors.</p>

<div class="card port" style="left:0">
  <div class="ph" role="img" aria-label="Modern apartment living room" style="background:linear-gradient(160deg,#e9e3da,#a79882 60%,#5d5145)"></div>
  <h3>Urban Living <b>Residences</b></h3>
  <p>reader will be distracted by the readable content of a page when looking at its layout. The point of using Lorem Ipsum.</p>
  <div class="meta"><span>Alder Point, NJ</span><span>View Details →</span></div>
</div>
<div class="card port" style="left:306px">
  <div class="ph" role="img" aria-label="Bright hospital corridor with seating" style="background:linear-gradient(160deg,#f4f5f6,#c9d0d7 60%,#7b8895)"></div>
  <h3>Horizon <b>Healthcare Center</b></h3>
  <p>reader will be distracted by the readable content of a page when looking at its layout. The point of using Lorem Ipsum.</p>
  <div class="meta"><span>Alder Point, NJ</span><span>View Details →</span></div>
</div>
<div class="card port" style="left:612px">
  <div class="ph" role="img" aria-label="Colourful commercial tower buildings" style="background:linear-gradient(180deg,#b9cde0,#8e9aa6 50%,#b8674e)"></div>
  <h3>Commerce <b>Park Towers</b></h3>
  <p>reader will be distracted by the readable content of a page when looking at its layout. The point of using Lorem Ipsum.</p>
  <div class="meta"><span>Alder Point, NJ</span><span>View Details →</span></div>
</div>
<div class="card port" style="left:918px">
  <div class="ph" role="img" aria-label="Two colleagues working together at a laptop" style="background:linear-gradient(160deg,#f1efec,#d6c8b6 55%,#9c7f5f)"></div>
  <h3>Investment <b>Corporation</b></h3>
  <p>reader will be distracted by the readable content of a page when looking at its layout. The point of using Lorem Ipsum.</p>
  <div class="meta"><span>Alder Point, NJ</span><span>View Details →</span></div>
</div>

<svg class="abs" style="left:0;top:3188px" width="1200" height="62" viewBox="0 0 1200 62">
  <polygon points="1200,0 1200,62 850,62" fill="#e0202a"/>
</svg>

<!-- Testimonials -->
<section class="abs testi-bg" role="img" aria-label="Dark muted photo of business people meeting"></section>
<h2 class="abs testi-title">TESTIMONIALS</h2>

<div class="tcard" style="left:-156px"><span class="quote">”</span><h4 style="margin-top:80px">&nbsp;</h4><p>dummy text of the industry. Lorem dustry's standard the 1500s typing has been.</p></div>
<div class="tcard" style="left:150px"><div class="avatar" role="img" aria-label="Client portrait"></div><span class="stars">★★★☆☆</span><span class="quote r">”</span><h4>Lena Marsh</h4><p>Lorem Ipsum is simply dummy text of the printing and typesetting industry. Lorem Ipsum has been the industry's standard dummy text ever since the 1500s.</p></div>
<div class="tcard" style="left:458px"><div class="avatar" role="img" aria-label="Client portrait"></div><span class="stars">★★★☆☆</span><span class="quote">”</span><h4>Lena Marsh</h4><p>Lorem Ipsum is simply dummy text of the printing and typesetting industry. Lorem Ipsum has been the industry's standard dummy text ever since the 1500s. Lorem Ipsum is simply dummy text of the printing.</p></div>
<div class="tcard" style="left:765px"><div class="avatar" role="img" aria-label="Client portrait"></div><span class="stars">★★★☆☆</span><span class="quote r">”</span><h4>Lena Marsh</h4><p>Lorem Ipsum is simply dummy text of the printing and typesetting industry. Lorem Ipsum has been the industry's standard dummy text ever since the 1500s. Lorem Ipsum has.</p></div>
<div class="tcard" style="left:1072px"><div class="avatar" role="img" aria-label="Client portrait"></div><span class="stars">★★★☆☆</span><span class="quote">”</span><h4>Lena Marsh</h4><p>Lorem Ipsum is simply printing and types Ipsum has been the dummy text ever si Ipsum is simply dur and typesetting ind</p></div>
<div class="abs pager"><i></i><i></i><i class="on"></i><i></i><i></i></div>

<!-- Contact -->
<svg class="abs" style="left:0;top:3738px" width="1200" height="80" viewBox="0 0 1200 80">
  <polygon points="0,0 1200,0 0,80" fill="#ececec"/>
</svg>
<div class="abs form-card">
  <h2>Contact <span class="red">us</span></h2>
  <label>Full Name</label><div class="field"></div>
  <label>Phone Number</label><div class="field"></div>
  <label>How can we help?</label><div class="field tall"></div>
  <div class="submit">Submit Now</div>
</div>
<div class="abs contact-text">
  <h2>Ready to Make <span class="red">Your Next Move?</span></h2>
  <p class="lead">Reach out to discuss partnership opportunities or learn more about our investment approach.</p>
  <h4>Why Choose <span class="red" style="font-weight:600">VELMORA</span></h4>
  <div class="why"><svg width="18" height="16" viewBox="0 0 18 16" fill="none" stroke="#e0202a" stroke-width="2.5"><path d="M2 8l5 5L16 2"/></svg><div><strong>Vertical Integration</strong><span>Complete Control Over The Investment Process From Acquisition Through Management And Disposition.</span></div></div>
  <div class="why"><svg width="18" height="16" viewBox="0 0 18 16" fill="none" stroke="#e0202a" stroke-width="2.5"><path d="M2 8l5 5L16 2"/></svg><div><strong>Strategic Partnerships</strong><span>Strong Relationships With Banks, Brokers, And Institutional Partners For Deal Flow And Financing.</span></div></div>
  <div class="why"><svg width="18" height="16" viewBox="0 0 18 16" fill="none" stroke="#e0202a" stroke-width="2.5"><path d="M2 8l5 5L16 2"/></svg><div><strong>Risk Management</strong><span>Disciplined Approach To Risk Assessment And Mitigation Across All Investment Decisions.</span></div></div>
</div>
<svg class="abs" style="left:0;top:4322px" width="1200" height="117" viewBox="0 0 1200 117">
  <polygon points="0,0 0,117 600,117" fill="#e0202a"/>
  <polygon points="1200,0 1200,117 520,117" fill="#e6e6e6"/>
</svg>

<!-- Footer -->
<footer class="abs footer">
  <div class="brand"><span class="mark"></span>VELMORA</div>
  <p class="about">Lorem Ipsum is simply dummy text of the printing and typesetting industry.</p>
  <div class="follow">Follow Us: <i></i><i class="r"></i><i></i></div>
  <div class="fcol" style="left:410px"><h4>Quick Links</h4><ul><li>Home</li><li>Our Story</li><li>Investment Strategy</li><li>What Sets Us Apart</li><li>Our Portfolio</li><li>Contact</li></ul></div>
  <div class="fcol" style="left:614px"><h4>Use Full links</h4><ul><li>Four Decades of Experience</li><li>Partnership Approach</li><li>Innovative Solutions</li></ul></div>
  <div class="fcol" style="left:863px"><h4 style="margin-bottom:16px">Contact Us</h4>
    <div class="contact-row"><span class="ic"><svg width="14" height="16" viewBox="0 0 14 16" fill="none" stroke="#ddd" stroke-width="1.8"><path d="M7 15s5-5 5-9A5 5 0 0 0 2 6c0 4 5 9 5 9z"/><circle cx="7" cy="6" r="1.8"/></svg></span><span>Alder Point, NJ</span></div>
    <div class="contact-row"><span class="ic r"><svg width="14" height="14" viewBox="0 0 14 14" fill="#fff"><path d="M3 1l2.5 3-1.5 1.5a8 8 0 0 0 4.5 4.5L10 8.5l3 2.5-1.5 2C6 13 1 8 1 2.5z"/></svg></span><span>Phone: <b>(555)-014 2280</b></span></div>
    <div class="contact-row"><span class="ic"><svg width="14" height="12" viewBox="0 0 14 12" fill="none" stroke="#ddd" stroke-width="1.6"><rect x="1" y="1" width="12" height="10"/><path d="M1 2l6 5 6-5"/></svg></span><span>hello@velmora.com</span></div>
  </div>
  <div class="copy">© 2025 Velmora Partners. All Rights Reserved.</div>
</footer>

</body>
</html>
```